Professional/Sleek card design for athletic apparel brand

Athletic apparel brand. Mainly focused on lifting weights/gym workouts. Logo and brand are already created. Must use brand logo and name. Creativity is welcome. Looking for a clean, modern, and sexy design.

```html
<!DOCTYPE html>
<html lang="en">
<head>
<meta charset="UTF-8">
<title>Iron and Grit – Business Card</title>
<link rel="stylesheet" href="https://fonts.googleapis.com/css2?family=Russo+One&family=Montserrat:wght@400;500;700&display=swap">
<style>
  :root {
    --backdrop: #2b2d30;
    --card-white: #ffffff;
    --card-black: #2a2a2a;
    --band: #2f2f2f;
    --ink: #1c1c1c;
    --ink-soft: #6b6b6b;
    --on-dark: #e9e9e9;
    --brand-font: "Russo One", sans-serif;
    --body-font: "Montserrat", sans-serif;
  }
  * { box-sizing: border-box; margin: 0; padding: 0; }
  html, body { width: 1200px; height: 952px; overflow: hidden; }
  body {
    background: var(--backdrop);
    position: relative;
    font-family: var(--body-font);
  }
  .card {
    position: absolute;
    width: 560px;
    height: 320px;
    border-radius: 26px;
    overflow: hidden;
    box-shadow: 0 14px 30px rgba(0,0,0,0.45);
  }

  /* Back of card */
  .card--back {
    left: 580px;
    top: 150px;
    background: var(--card-black);
    display: flex;
    align-items: center;
    justify-content: center;
  }
  .back-brand {
    display: flex;
    align-items: center;
    gap: 14px;
  }
  .back-brand__dot {
    width: 22px; height: 22px;
    border-radius: 50%;
    background: var(--on-dark);
  }
  .back-brand__name {
    font-family: var(--brand-font);
    font-size: 38px;
    line-height: 1;
    color: var(--on-dark);
    letter-spacing: 1px;
  }

  /* Front of card */
  .card--front {
    left: 60px;
    top: 500px;
    background: var(--card-white);
  }
  .front-brand {
    position: absolute;
    left: 110px;
    top: 34px;
    font-family: var(--brand-font);
    font-size: 30px;
    line-height: 1;
    color: var(--ink);
    letter-spacing: 0.5px;
  }
  .contact-band {
    position: absolute;
    left: 0;
    top: 96px;
    width: 290px;
    height: 150px;
    background: var(--band);
    border-radius: 0 0 80px 0;
  }
  .contact-list {
    list-style: none;
    position: absolute;
    left: 26px;
    top: 18px;
    display: flex;
    flex-direction: column;
    gap: 9px;
  }
  .contact-list li {
    display: flex;
    align-items: flex-start;
    gap: 10px;
    font-size: 12px;
    line-height: 1.35;
    color: var(--on-dark);
  }
  .contact-list svg { width: 12px; height: 12px; flex: none; margin-top: 2px; fill: var(--on-dark); }
  .holder {
    position: absolute;
    right: 36px;
    top: 112px;
    text-align: right;
    max-width: 220px;
  }
  .holder__name {
    font-size: 18px;
    font-weight: 500;
    color: var(--ink);
    letter-spacing: 0.4px;
    white-space: nowrap;
  }
  .holder__name strong { font-weight: 700; }
  .holder__title {
    margin-top: 4px;
    font-size: 13px;
    color: var(--ink-soft);
    display: inline-block;
    padding-bottom: 6px;
    border-bottom: 1.5px solid var(--ink);
  }
</style>
</head>
<body>

  <section class="card card--back" aria-label="Card back">
    <div class="back-brand">
      <span class="back-brand__dot"></span>
      <span class="back-brand__name">IRON AND GRIT</span>
    </div>
  </section>

  <section class="card card--front" aria-label="Card front">
    <div class="front-brand">IRON AND GRIT</div>

    <div class="contact-band">
      <ul class="contact-list">
        <li>
          <svg viewBox="0 0 12 12"><path d="M6 0a4 4 0 0 0-4 4c0 3 4 8 4 8s4-5 4-8a4 4 0 0 0-4-4zm0 5.6A1.6 1.6 0 1 1 6 2.4a1.6 1.6 0 0 1 0 3.2z"/></svg>
          <span>48 Harbor Lane Eastwood<br>NSW 000 USA</span>
        </li>
        <li>
          <svg viewBox="0 0 12 12"><path d="M2.4 0.5l2 2.2-1 1.4a7 7 0 0 0 4.5 4.5l1.4-1 2.2 2-1.2 1.9C5.5 11.6 0.4 6.5 0.5 1.7z"/></svg>
          <span>+00 987 654 32</span>
        </li>
        <li>
          <svg viewBox="0 0 12 12"><path d="M0 2h12v8H0zm1 1v.4l5 3.3 5-3.3V3zm0 1.6V9h10V4.6L6 7.9z"/></svg>
          <span>hello@ironandgrit.com</span>
        </li>
        <li>
          <svg viewBox="0 0 12 12"><path d="M6 0l5 6H7.5v6h-3V6H1z"/></svg>
          <span>www.ironandgrit.com</span>
        </li>
      </ul>
    </div>

    <div class="holder">
      <div class="holder__name">DANIEL R. <strong>MORENO</strong></div>
      <div class="holder__title">Managing Director</div>
    </div>
  </section>

</body>
</html>
```